Infographic comparing two personal financial success strategies

Need an infographic designed comparing typical financial planning advice to my proprietary wealth platform "The Vantage Harbor Method". My system is designed primarily for business owners, professionals and executives who aspire to a work-optional lifestyle. I would like designs that use my websites color palette (www.quillmorecap.com) and include my logo. The final design should highlight the differences between the typical approach and the benefits of the "The Vantage Harbor Method".

Target Market(s)

Business owners, professionals (doctors, lawyers, accoutnants, and business executives

Industry/Entity Type

Financial Service

Font styles to use
Sans Serif

Colors
33a6d7
0455a3
cee9f5

```html
<!DOCTYPE html>
<html lang="en">
<head>
<meta charset="utf-8">
<title>The Vantage Harbor Method™ Infographic</title>
<link href="https://fonts.googleapis.com/css2?family=PT+Sans:wght@400;700&display=swap" rel="stylesheet">
<style>
  :root{
    --stage:#e6e5e3;
    --paper:#ffffff;
    --navy:#1b2a6b;
    --deep:#0455a3;
    --sky:#33a6d7;
    --mist:#cee9f5;
    --royal:#1d3f8c;
    --ink:#2a2a3a;
  }
  *{box-sizing:border-box;margin:0;padding:0}
  html,body{width:1200px;height:1200px;overflow:hidden}
  body{background:var(--stage);font-family:"PT Sans",sans-serif;position:relative;color:var(--ink)}

  .infographic{position:absolute;left:179px;top:166px;width:843px;height:600px;background:var(--paper);box-shadow:0 1px 4px rgba(0,0,0,.12)}
  .infographic__title{position:absolute;top:50px;left:0;right:0;text-align:center;font-size:21px;font-weight:700;color:var(--navy)}
  .infographic__wheels{position:absolute;inset:0;width:843px;height:600px}
  .wheel text{font-family:"PT Sans",sans-serif;fill:#fff;dominant-baseline:middle}
  .wheel .head{font-size:15.5px;font-weight:700}
  .wheel .body{font-size:10.5px}
  .wheel .core{font-size:20px;font-weight:700}
  .wheel .mid{text-anchor:middle}

  .brand{position:absolute;display:flex;align-items:center;gap:6px}
  .brand__dot{border-radius:50%;border:2.5px solid var(--deep);flex:none}
  .brand__name{font-weight:700;color:var(--navy);line-height:1;letter-spacing:.2px}
  .brand__tag{font-size:8px;color:var(--navy);line-height:1.1}
  .infographic .brand{left:43px;top:530px}
  .infographic .brand__dot{width:30px;height:30px}
  .infographic .brand__name{font-size:13px}
  .infographic__url{position:absolute;right:49px;top:545px;font-size:10.5px;color:var(--navy)}

  .card{position:absolute;top:776px;width:422px;height:274px;box-shadow:0 1px 4px rgba(0,0,0,.12);overflow:hidden}
  .card--front{left:178px;background:var(--paper)}
  .card--back{left:600px;background:var(--paper)}

  .card__lockup{position:absolute;left:0;right:0;top:52px;text-align:center}
  .card__lockup .brand__dot{width:88px;height:88px;border-width:5px;border-color:var(--deep);margin:0 auto 10px}
  .card__lockup .brand__name{font-size:16px;display:block}
  .card__lockup .brand__tag{font-size:10.5px;margin-top:2px}
  .card__band{position:absolute;left:0;right:0;bottom:0;height:54px;background:linear-gradient(90deg,var(--sky),var(--deep) 55%,var(--royal))}
  .card__band-mark{position:absolute;left:42px;top:8px;width:38px;height:38px;border-radius:50%;border:2px solid rgba(255,255,255,.35)}
  .card__band-url{position:absolute;right:42px;top:18px;color:#fff;font-size:12.5px;letter-spacing:.3px}

  .card__panel{position:absolute;left:0;right:0;top:0;height:220px;background:linear-gradient(100deg,var(--royal) 0%,var(--deep) 55%,var(--sky) 100%)}
  .card__name{position:absolute;left:42px;top:36px;color:#fff;font-size:16.5px;font-weight:700;letter-spacing:.2px}
  .contact{position:absolute;left:40px;top:96px;list-style:none;color:#fff;font-size:12.5px;letter-spacing:.3px}
  .contact li{display:flex;align-items:center;gap:5px;height:21px}
  .contact svg{width:11px;height:11px;fill:#fff}
  .card--back .brand{left:42px;top:233px}
  .card--back .brand__dot{width:30px;height:30px}
  .card--back .brand__name{font-size:12.5px}
</style>
</head>
<body>

<section class="infographic">
  <h1 class="infographic__title">The Vantage Harbor Method™ Infographic</h1>

  <svg class="infographic__wheels" viewBox="224 208 1053 749" aria-label="Comparison wheels: The Vantage Harbor Method versus typical financial advice">
    <defs>
      <radialGradient id="blueFill" cx="50%" cy="50%" r="50%">
        <stop offset="0" stop-color="#3a9ee0"/>
        <stop offset=".55" stop-color="#1f74c4"/>
        <stop offset="1" stop-color="#0d4a9c"/>
      </radialGradient>
      <radialGradient id="blueCore" cx="50%" cy="50%" r="50%">
        <stop offset="0" stop-color="#40aee6"/>
        <stop offset="1" stop-color="#2a8fd2"/>
      </radialGradient>
      <radialGradient id="greyFill" cx="50%" cy="50%" r="50%">
        <stop offset="0" stop-color="#7a7a7a"/>
        <stop offset="1" stop-color="#666"/>
      </radialGradient>
    </defs>

    <g class="wheel wheel--method">
      <circle cx="498" cy="590" r="248" fill="url(#blueFill)"/>
      <g stroke="#fff" stroke-width="2">
        <line x1="590" y1="590" x2="746" y2="590"/>
        <line x1="551" y1="665" x2="639" y2="793"/>
        <line x1="445" y1="665" x2="357" y2="793"/>
        <line x1="406" y1="590" x2="250" y2="590"/>
        <line x1="452" y1="510" x2="374" y2="375"/>
        <line x1="544" y1="510" x2="622" y2="375"/>
      </g>
      <circle cx="498" cy="590" r="82" fill="none" stroke="#fff" stroke-width="18" stroke-dasharray="58.4 6" stroke-dashoffset="-3"/>
      <circle cx="498" cy="590" r="73" fill="url(#blueCore)"/>
      <text class="core mid" x="498" y="572">Vantage</text>
      <text class="core mid" x="498" y="593">Harbor</text>
      <text class="core mid" x="498" y="614">Method™</text>

      <text class="head mid" x="495" y="387">Cash Flow</text>
      <text class="body" x="455" y="406">Job,</text>
      <text class="body" x="455" y="421">Company,</text>
      <text class="body" x="455" y="436">Real-Estate,</text>
      <text class="body" x="455" y="451">Investments,</text>
      <text class="body" x="455" y="466">etc.</text>

      <text class="head mid" x="642" y="448">Cash Flow</text>
      <text class="head mid" x="642" y="465">Maximization</text>
      <text class="body" x="575" y="482">Get the most from your</text>
      <text class="body" x="575" y="494">money now, don't reduce</text>
      <text class="body" x="575" y="506">lifestyle</text>
      <text class="body" x="584" y="519">a. Reduce taxes</text>
      <text class="body" x="584" y="531">– Flow-through, RRSPs &amp; TFSAs</text>
      <text class="body" x="584" y="543">b. Recapture interest expense</text>
      <text class="body" x="584" y="556">– Use Opportunity Cost</text>

      <text class="head mid" x="650" y="613">Cash Flow</text>
      <text class="head mid" x="650" y="630">Protection</text>
      <text class="body" x="581" y="648">Protect &amp; Multiple the uses of</text>
      <text class="body" x="581" y="660">your money</text>
      <text class="body" x="590" y="675">a. Protect your income</text>
      <text class="body" x="590" y="689">b. Create guaranteed</text>
      <text class="body" x="590" y="701">savings</text>

      <text class="head mid" x="492" y="692">Cash Flow</text>
      <text class="head mid" x="492" y="709">Expansion</text>
      <text class="body" x="412" y="727">Multiple your income streams and</text>
      <text class="body" x="412" y="739">increase cash flow now</text>
      <text class="body" x="412" y="751">a. Regularly add new income streams</text>
      <text class="body" x="423" y="763">1. Dividend and interest paying</text>
      <text class="body" x="432" y="775">investments</text>
      <text class="body" x="441" y="787">• Direct &amp; In-direct Real-estate</text>
      <text class="body" x="441" y="798">• Private Business ownership</text>
      <text class="body" x="441" y="809">• Company Stocks</text>
      <text class="body" x="441" y="820">• Private Lending</text>

      <text class="head mid" x="350" y="633">Work because</text>
      <text class="head mid" x="350" y="651">you want to ...</text>
      <text class="head mid" x="350" y="669">not because</text>
      <text class="head mid" x="350" y="688">you have to!</text>

      <text class="head mid" x="340" y="495">BlueSky think</text>
      <text class="head mid" x="340" y="514">your goals,</text>
      <text class="head mid" x="340" y="532">dreams and life!</text>
    </g>

    <g class="wheel wheel--typical">
      <circle cx="1006" cy="590" r="248" fill="url(#greyFill)"/>
      <g stroke="#fff" stroke-width="2">
        <line x1="971" y1="505" x2="911" y2="361"/>
        <line x1="1041" y1="505" x2="1101" y2="361"/>
        <line x1="1091" y1="555" x2="1235" y2="495"/>
        <line x1="1091" y1="625" x2="1235" y2="685"/>
        <line x1="1041" y1="675" x2="1101" y2="819"/>
        <line x1="971" y1="675" x2="911" y2="819"/>
        <line x1="921" y1="625" x2="777" y2="685"/>
        <line x1="921" y1="555" x2="777" y2="495"/>
      </g>
      <circle cx="1006" cy="590" r="82" fill="none" stroke="#fff" stroke-width="18" stroke-dasharray="58.4 6" stroke-dashoffset="-3"/>
      <circle cx="1006" cy="590" r="73" fill="#727272"/>
      <text class="core mid" x="1006" y="569">Typical</text>
      <text class="core mid" x="1006" y="591">Financial</text>
      <text class="core mid" x="1006" y="613">Advice</text>

      <text class="head mid" x="1008" y="385">Make income</text>
      <text class="body" x="964" y="406">Job,</text>
      <text class="body" x="964" y="421">Company,</text>
      <text class="body" x="964" y="436">Real-Estate,</text>
      <text class="body" x="964" y="451">Investments,</text>
      <text class="body" x="964" y="466">etc.</text>

      <text class="head mid" x="1130" y="460">Pay Taxes</text>
      <text class="body mid" x="1130" y="476">Reduces income</text>
      <text class="body mid" x="1116" y="490">a. RRSP</text>

      <text class="head mid" x="1175" y="558">Pay interest</text>
      <text class="body mid" x="1175" y="575">(mortgage, car loan,</text>
      <text class="body mid" x="1168" y="587">credit cards, etc.)</text>
      <text class="body mid" x="1165" y="599">Reduces income</text>
      <text class="body mid" x="1173" y="614">a. Pay off faster</text>

      <text class="head mid" x="1135" y="681">Pay for lifestyle</text>
      <text class="body" x="1068" y="697">(food, shelter, vacations,</text>
      <text class="body" x="1068" y="709">recreation, education, etc.)</text>
      <text class="body" x="1068" y="721">Reduces income</text>
      <text class="body" x="1078" y="736">a. Cut back on spending</text>

      <text class="head mid" x="1006" y="741">Hope for good</text>
      <text class="head mid" x="1006" y="756">returns on</text>
      <text class="head mid" x="1006" y="771">what you can</text>
      <text class="head mid" x="1006" y="786">save</text>

      <text class="head mid" x="890" y="676">Hope nothing</text>
      <text class="head mid" x="890" y="693">bad happens</text>
      <text class="body" x="841" y="708">a. Laid-off, no work,</text>
      <text class="body" x="841" y="720">fired, company fails,</text>
      <text class="body" x="841" y="732">etc.</text>
      <text class="body" x="841" y="747">b. Can't work for</text>
      <text class="body" x="841" y="762">health reason(s)</text>

      <text class="head mid" x="842" y="571">Hope you don't</text>
      <text class="head mid" x="842" y="589">live too long in</text>
      <text class="head mid" x="842" y="606">retirement</text>

      <text class="head mid" x="881" y="454">Minimizes</text>
      <text class="head mid" x="881" y="471">future lifestyle</text>
      <text class="head mid" x="881" y="488">and dreams</text>
    </g>
  </svg>

  <div class="brand">
    <span class="brand__dot"></span>
    <div>
      <span class="brand__name">QUILLMORE CAPITAL</span>
      <div class="brand__tag">Wealth that works for you</div>
    </div>
  </div>
  <div class="infographic__url">www.quillmorecap.com</div>
</section>

<section class="card card--front">
  <div class="card__lockup">
    <div class="brand__dot"></div>
    <span class="brand__name">QUILLMORE CAPITAL</span>
    <div class="brand__tag">Wealth that works for you</div>
  </div>
  <div class="card__band">
    <span class="card__band-mark"></span>
    <span class="card__band-url">www.quillmorecap.com</span>
  </div>
</section>

<section class="card card--back">
  <div class="card__panel">
    <div class="card__name">Daniel R. Okafor B.Comm, CCS</div>
    <ul class="contact">
      <li><svg viewBox="0 0 12 12"><path d="M3 1l2 2.5-1.2 1.3c.7 1.5 1.8 2.6 3.3 3.3L8.4 6.9 11 9l-1.3 2C5.2 10.6 1.4 6.8 1 2.3z"/></svg>(555) 014-2290</li>
      <li><svg viewBox="0 0 12 12"><path d="M0 2.5h12v7H0z M0 2.5l6 4 6-4" stroke="#1d4f9c" stroke-width=".8"/></svg>e-mail</li>
      <li><svg viewBox="0 0 12 12"><path d="M6 .8L0 6h1.6v5.2h3.2V8h2.4v3.2h3.2V6H12z"/></svg>address</li>
    </ul>
  </div>
  <div class="brand">
    <span class="brand__dot"></span>
    <div>
      <span class="brand__name">QUILLMORE CAPITAL</span>
      <div class="brand__tag">Wealth that works for you</div>
    </div>
  </div>
</section>

</body>
</html>
```